Manufacturing Company WordPress Website Design

Looking for a modern WordPress design for a manufacturer of oil separation and coolant recycling products called BrightVane. This is a business-to-business marketer in the industrial manufacturing sector. BrightVane sells to CNC manufacturing companies and their products are known as some of the best tools in the world for skimming and separating floating oils, metallic fines, and other contaminants from industrial process fluids.

The winning design will be based on a responsive WP theme. Include the theme name if your design is selected by the client. Provide Home, Product and Case Study page views with your submission.

THE BRIGHTVANE BRAND
The BrightVane brand is all about connection and partnership. They are down-to-earth, relatable, helpful and fun to hang out with. The brand voice is humble, authentic and helpful and they are driven by connection, togetherness and inclusion.

The BrightVane target audience is plant managers, enterprise engineers and business owners in CNC machining manufacturing companies across a variety of industries (automotive, aerospace, energy, medical and transportation).

BrightVane is looking for a clean, modern website that better represents their brand with a more polished and professional design. It should be:
- responsive and mobile-friendly
- easily findable for key search criteria
- a source for improved lead generation for prospective sales
- more easily editable

A design that is oriented toward these goals will be selected as the winner.

The winning designer may be chosen to code the website, or to code the initial pages in the concept design.

Current Website:
https://brightvane-example.com/index.html

Competitors:
https://www.tovlex-example.com/
https://www.mundrel-example.com/
https://www.kelvaro-example.com/

Sites We Like:
https://northgatesteelworks-example.com/
- we like the clean layout of the home page in a grid-like design, simple header and footer, the parallax scrolling, and the mobile responsiveness.

https://www.tovlex-example.com/fluid-filtration/sentinel-coolant-recycling-systems/
- we like the way the content is presented on the Tovlex product page - specifically, we like the use of the tabs below the main product images to present a lot of content without it looking overwhelmingly busy.

https://dunmorepanel-example.com/healthcare/westbrook-care-hospital/
- we like the way Dunmore Panel presents their cases studies with a combination of useful information highlighted by informative icons and pictures to present key statistics in the case study. We would like the BrightVane case studies to almost feel like an infographic presentation on the website.

Target Market(s)

Industry/Entity Type

Industrial

Coding

Coded - Design and coding required

Number of Pages Required

3 page

Font styles to use
Sans Serif
Other font styles liked:
• DINPro is used on all collateral - see brand guidelines

Requirements
Must have
• See the brand guidelines file attached for colors and logo usage

```html
<!DOCTYPE html>
<html lang="en">
<head>
<meta charset="utf-8">
<title>BrightVane – Oil Separation</title>
<link rel="stylesheet" href="https://fonts.googleapis.com/css2?family=Roboto:wght@400;500;700&display=swap">
<style>
:root{
  --navy:#0b3d7e;
  --navy-dark:#08305f;
  --ink:#1b1b1b;
  --text:#444;
  --muted:#8a8a8a;
  --line:#dcdcdc;
  --green:#5aa62b;
  --star:#f28a1e;
  --soft:#f4f5f7;
}
*{box-sizing:border-box;margin:0;padding:0}
html,body{width:1200px;height:3750px;overflow:hidden;background:#fff}
body{font-family:'Roboto',sans-serif;color:var(--ink);position:relative}
.abs{position:absolute}
a{color:inherit;text-decoration:none}

/* top bar */
.topbar{left:0;top:0;width:1200px;height:32px;background:var(--navy);color:#fff;font-size:11px}
.topbar span{position:absolute;top:10px;display:flex;align-items:center;gap:8px}
.topbar svg{width:11px;height:11px}
.social{display:flex;gap:16px;font-weight:700}
.social i{font-style:normal}

/* header */
.logo{left:184px;top:46px;display:flex;align-items:center;gap:10px}
.logo-dot{width:46px;height:46px;border-radius:50%;background:var(--navy)}
.logo-name{font-size:26px;font-weight:700;color:var(--navy)}
.nav{left:428px;top:65px;display:flex;gap:22px;font-size:15px;color:#222}
.login{left:945px;top:59px;width:71px;height:32px;border:1.5px solid var(--navy);border-radius:16px;color:var(--navy);font-size:12px;font-weight:700;display:flex;align-items:center;justify-content:center}

/* hero */
.hero-photo{left:64px;top:32px;width:1136px;height:543px;background:linear-gradient(90deg,#fff 0%,rgba(255,255,255,.9) 22%,rgba(222,170,120,.55) 45%,#6a82a6 70%,#2c4f80 100%)}
.hero-kicker{left:183px;top:190px;font-size:23px;font-weight:700;color:var(--navy)}
.hero-title{left:182px;top:218px;font-size:52px;font-weight:700;color:#111}
.hero-text{left:183px;top:300px;width:340px;font-size:14px;line-height:22px;color:#333}
.btn{display:flex;align-items:center;justify-content:center;border-radius:24px;font-size:12px;font-weight:700}
.btn-solid{background:var(--navy);color:#fff}
.btn-ghost{border:1.5px solid var(--navy);color:var(--navy);background:#fff}

/* about */
.about-photo{left:176px;top:651px;width:412px;height:327px;background:linear-gradient(135deg,#4b5663,#c9793a 55%,#3d4552)}
.h2{font-size:32px;font-weight:700;color:#111}
.about-text{left:613px;top:720px;width:335px;font-size:14px;line-height:22.5px;color:#333}
.center{left:0;width:1200px;text-align:center}
.sub{font-size:14px;line-height:22px;color:#444}

/* products */
.card{background:#fff;box-shadow:0 4px 18px rgba(0,0,0,.09)}
.card-img{height:211px;background:linear-gradient(180deg,#dcdcdc,#e6e6e6)}
.card-body{padding:22px}
.card h3{font-size:16px;font-weight:700;margin-bottom:14px}
.card p{font-size:13px;line-height:19.5px;color:#444;height:118px}
.card a{font-size:14px;font-weight:700;color:var(--navy)}
.arrow{width:34px;height:34px;border-radius:50%;display:flex;align-items:center;justify-content:center}
.arrow-ghost{border:1.5px solid #777}
.arrow-solid{background:var(--navy)}
.dots{display:flex;gap:16px;align-items:center}
.dots b{width:6px;height:6px;border-radius:50%;background:#b5b5b5;display:block}
.dots b.on{background:var(--navy);box-shadow:0 0 0 5px #e5ebf3}

/* trusted */
.brands{left:183px;top:1880px;width:835px;display:flex;justify-content:space-between;align-items:center}
.brand{font-size:17px;font-weight:700;color:#222}

/* roi */
.roi{left:0;top:2001px;width:1200px;height:343px;background:linear-gradient(180deg,#0c3f82,#0a376f)}

/* testimonials */
.tcard{background:#fff;box-shadow:0 4px 18px rgba(0,0,0,.08);padding:40px 20px 0}
.tcard.on{background:var(--navy);color:#fff;box-shadow:0 10px 24px rgba(11,61,126,.35)}
.tcard p{font-size:12px;line-height:19px;height:62px}
.tcard.on p{font-size:13px}
.tfoot{border-top:1px solid #ddd;margin-top:10px;padding-top:10px;display:flex;justify-content:space-between;font-size:11px}
.tcard.on .tfoot{border-color:rgba(255,255,255,.3)}
.tfoot strong{display:block;font-size:12px;margin-bottom:4px}
.stars{color:var(--star);font-size:11px;letter-spacing:1px}
.avatar{width:54px;height:54px;border-radius:50%;background:#9aa6b3;border:3px solid #fff;box-shadow:0 2px 6px rgba(0,0,0,.2)}

/* contact */
.muted-h{font-size:21px;font-weight:700;color:#a9a9a9}
.info{display:flex;gap:20px;font-size:15px;line-height:22px;color:#222}
.info svg{width:16px;height:16px;flex:none;margin-top:3px}
.form{left:625px;top:2916px;width:375px;height:555px;background:#fff;box-shadow:0 4px 24px rgba(0,0,0,.08);padding:42px 36px}
.field{border-bottom:1px solid var(--line);height:82px;padding-top:0;margin-bottom:0}
.field label{display:block;font-size:12px;font-weight:500;color:#222;margin-bottom:10px;padding-top:0}
.field div{font-size:15px;color:var(--muted)}
.field+.field{padding-top:0}
.submit{width:304px;height:55px;background:var(--navy);color:#fff;font-size:16px;font-weight:700;border-radius:4px;display:flex;align-items:center;justify-content:center}

/* footer */
.foot{font-size:11px;color:#222}
.foot-links{left:183px;top:3553px;display:flex;gap:46px}
.foot-rule{left:183px;top:3598px;width:834px;height:1px;background:#bbb}
.legal{left:763px;top:3621px;display:flex;gap:34px;color:var(--navy);font-size:10px}
</style>
</head>
<body>

<!-- top bar -->
<div class="abs topbar">
  <span style="left:186px"><svg viewBox="0 0 24 24" fill="none" stroke="#fff" stroke-width="2"><path d="M5 3h4l2 5-3 2a12 12 0 0 0 6 6l2-3 5 2v4a2 2 0 0 1-2 2A17 17 0 0 1 3 5a2 2 0 0 1 2-2z"/></svg>(555) 014-2290</span>
  <span style="left:332px"><svg viewBox="0 0 24 24" fill="none" stroke="#fff" stroke-width="2"><rect x="3" y="5" width="18" height="14"/><path d="M3 5l9 8 9-8"/></svg>sales@brightvane-example.com</span>
  <span style="left:690px"><svg viewBox="0 0 24 24" fill="none" stroke="#fff" stroke-width="2"><circle cx="12" cy="12" r="9"/><path d="M3 12h18M12 3c3 3 3 15 0 18M12 3c-3 3-3 15 0 18"/></svg>www.brightvane-example.com</span>
  <span style="left:862px">Follow Us:</span>
  <span class="social" style="left:928px"><i>f</i><i>t</i><i>ig</i><i>in</i></span>
</div>

<!-- hero -->
<div class="abs hero-photo" role="img" aria-label="Engineer in hard hat and safety glasses checking a clipboard beside industrial equipment"></div>
<div class="abs logo"><div class="logo-dot"></div><div class="logo-name">BrightVane</div></div>
<nav class="abs nav"><a>Home</a><a>Benefits</a><a>Industries Served</a><a>About us</a><a>Service &amp; Support</a></nav>
<a class="abs login">Login</a>

<div class="abs hero-kicker">The Global Leader in</div>
<h1 class="abs hero-title">Oil Separation</h1>
<p class="abs hero-text">Lorem ipsum dolor sit amet, consectetur smod tempor incididunt.</p>
<a class="abs btn btn-solid" style="left:184px;top:370px;width:122px;height:44px">Read More</a>
<a class="abs btn btn-ghost" style="left:319px;top:370px;width:122px;height:44px">Products</a>

<!-- about -->
<div class="abs about-photo" role="img" aria-label="Engineer in white hard hat and safety vest holding a tablet on the factory floor"></div>
<h2 class="abs h2" style="left:613px;top:658px">About Us</h2>
<p class="abs about-text">Since 1998, the BrightVane product line has been producing some of the best solutions in the world for the management of industrial fluids. Our products combine innovative design, rugged durability and performance. In partnering with us, you can rest assured that you have invested in the best But we don't expect you to take our word for it. We have seven separate patents.</p>
<a class="abs btn btn-solid" style="left:613px;top:929px;width:160px;height:49px">View Our History</a>

<!-- products -->
<h2 class="abs h2 center" style="top:1050px">Our Products</h2>
<p class="abs sub center" style="top:1111px">Lorem ipsum dolor sit amet consectetur adipisicing elit sed do eiusmod tempor<br>incididunt ut labore et dolore magna aliqua.</p>

<div class="abs arrow arrow-ghost" style="left:111px;top:1410px"><svg width="12" height="12" viewBox="0 0 12 12"><path d="M8 2L4 6l4 4" fill="none" stroke="#555" stroke-width="1.6"/></svg></div>
<div class="abs arrow arrow-solid" style="left:1055px;top:1410px"><svg width="12" height="12" viewBox="0 0 12 12"><path d="M4 2l4 4-4 4" fill="none" stroke="#fff" stroke-width="1.8"/></svg></div>

<div class="abs card" style="left:183px;top:1203px;width:263px;height:445px">
  <div class="card-img" role="img" aria-label="Blue coolant recycling system unit with steel drum"></div>
  <div class="card-body"><h3>Coolant Recycling Systems</h3>
  <p>The FlowCycle™ Coolant Recycling Systems are based on decades-long successful fluid treatment practices, using the award-winning, multipatented BrightVane® Systems approach to solving problems.</p>
  <a>Read More</a></div>
</div>
<div class="abs card" style="left:469px;top:1203px;width:262px;height:445px">
  <div class="card-img" role="img" aria-label="Pair of clear cylindrical magnetic separators"></div>
  <div class="card-body"><h3>Magnetic Separators</h3>
  <p>BrightVane magnetic separators fit with our core philosophies: providing products that eliminate the use of filter consumables, are easy to implement, simple to operate, and require minimal maintenance.</p>
  <a>Read More</a></div>
</div>
<div class="abs card" style="left:753px;top:1203px;width:263px;height:445px">
  <div class="card-img" role="img" aria-label="Blue oil water separator tank with drum"></div>
  <div class="card-body"><h3>Oil Water Separators</h3>
  <p>BrightVane The BrightVane "non-clogging" design allows for the separation of oils and settling of solids in one step.of filter consumables, are easy to implement, simple to operate.</p>
  <a>Read More</a></div>
</div>

<div class="abs dots" style="left:564px;top:1718px"><b class="on"></b><b></b><b></b><b></b></div>

<!-- trusted -->
<h2 class="abs center" style="top:1803px;font-size:29px;font-weight:700">Trusted By</h2>
<svg class="abs" style="left:120px;top:1891px" width="14" height="16" viewBox="0 0 14 16"><path d="M10 2L4 8l6 6" fill="none" stroke="#222" stroke-width="2.2"/></svg>
<svg class="abs" style="left:1066px;top:1891px" width="14" height="16" viewBox="0 0 14 16"><path d="M4 2l6 6-6 6" fill="none" stroke="#222" stroke-width="2.2"/></svg>
<div class="abs brands">
  <span class="brand">Arlen</span><span class="brand">Hestmark</span><span class="brand">Valcrest</span><span class="brand">Dorvel</span><span class="brand">Trenwick</span><span class="brand">Petralis</span>
</div>

<!-- roi -->
<section class="abs roi" role="img" aria-label="Dark blue tinted photo of industrial workshop"></section>
<h2 class="abs center" style="top:2068px;font-size:32px;font-weight:700;color:#fff">ROI Calculator</h2>
<p class="abs center" style="top:2137px;font-size:14.5px;line-height:20px;color:#fff">Lorem ipsum dolor sit amet consectetur adipisicing elit sed do eiusmod tempor incididunt ut labore<br>etdolore magna aliqua Ut enim ad minim veniam quis nostrud exercitation ullamco laboris nisi ut aliquip<br>ex ea commodo consequat Duis aute irure dolor.</p>
<a class="abs btn" style="left:539px;top:2228px;width:122px;height:42px;border:1.5px solid #fff;color:#fff;font-size:14px">Calculate</a>

<!-- testimonials -->
<h2 class="abs h2 center" style="top:2414px">Testimonials</h2>
<p class="abs sub center" style="top:2480px">Lorem ipsum dolor sit amet consectetur adipisicing elit sed do eiusmod tempor<br>incididunt ut labore et dolore magna aliqua.</p>

<div class="abs arrow" style="left:136px;top:2664px;width:18px;height:18px;border:1px solid #666"><svg width="8" height="8" viewBox="0 0 8 8"><path d="M5 1L2 4l3 3" fill="none" stroke="#555" stroke-width="1.2"/></svg></div>
<div class="abs arrow arrow-solid" style="left:1048px;top:2664px;width:18px;height:18px"><svg width="8" height="8" viewBox="0 0 8 8"><path d="M3 1l3 3-3 3" fill="none" stroke="#fff" stroke-width="1.4"/></svg></div>

<div class="abs tcard on" style="left:183px;top:2587px;width:263px;height:172px">
  <p>Lorem ipsum dolor sit amet, consec tetur adipiscing elit, sed do eiusm od tempor incidunt ut labore.</p>
  <div class="tfoot"><div><strong>John Doe</strong>Funder</div><div class="stars">★★★★☆</div></div>
</div>
<div class="abs tcard" style="left:469px;top:2587px;width:262px;height:172px">
  <p>Lorem ipsum dolor sit amet, consectetur adipiscing elit, sed do eiusmod tempor incidunt ut labore et dolore.</p>
  <div class="tfoot"><div><strong>John Doe</strong>MD</div><div class="stars">★★★★★</div></div>
</div>
<div class="abs tcard" style="left:753px;top:2587px;width:263px;height:172px">
  <p>Lorem ipsum dolor sit amet, consectetur adipiscing elit, sed do eiusmod tempor incidunt ut labore et dolore.</p>
  <div class="tfoot"><div><strong>John Doe</strong>CTO</div><div class="stars">★★★★★</div></div>
</div>
<div class="abs avatar" style="left:205px;top:2559px" role="img" aria-label="Customer portrait"></div>
<div class="abs avatar" style="left:490px;top:2559px;background:#7d8590" role="img" aria-label="Customer portrait"></div>
<div class="abs avatar" style="left:772px;top:2559px;background:#b69a7c" role="img" aria-label="Customer portrait"></div>

<div class="abs dots" style="left:564px;top:2822px"><b class="on"></b><b></b><b></b><b></b></div>

<!-- contact -->
<h2 class="abs h2" style="left:182px;top:2910px">Get In Touch</h2>
<p class="abs" style="left:182px;top:2967px;width:360px;font-size:14.5px;line-height:22.5px;color:#444">Lorem ipsum dolor sit amet, consectetur adipisicing elit, sed do eiusmod tempor incididunt ut labore et dolore magna aliqua.</p>

<div class="abs muted-h" style="left:182px;top:3070px">Location</div>
<div class="abs info" style="left:182px;top:3111px"><svg viewBox="0 0 24 24" fill="none" stroke="#222" stroke-width="1.6"><path d="M12 22s7-7 7-12a7 7 0 0 0-14 0c0 5 7 12 7 12z"/><circle cx="12" cy="10" r="2.5"/></svg><div>Northfield Separators, Inc.<br>1450 Harlow Avenue Fairview, WI 53090</div></div>

<div class="abs muted-h" style="left:182px;top:3190px">Need Help?</div>
<div class="abs info" style="left:182px;top:3236px"><svg viewBox="0 0 24 24" fill="none" stroke="#222" stroke-width="1.6"><rect x="3" y="5" width="18" height="14"/><path d="M3 5l9 8 9-8"/></svg><div>sales@brightvane-example.com</div></div>

<div class="abs muted-h" style="left:182px;top:3287px">Feel like Talking</div>
<div class="abs info" style="left:182px;top:3332px"><svg viewBox="0 0 24 24" fill="none" stroke="#222" stroke-width="1.6"><path d="M5 3h4l2 5-3 2a12 12 0 0 0 6 6l2-3 5 2v4a2 2 0 0 1-2 2A17 17 0 0 1 3 5a2 2 0 0 1 2-2z"/></svg><div>(555) 014-2290</div></div>

<form class="abs form">
  <div class="field"><label>Your name</label><div>John Doe</div></div>
  <div class="field" style="padding-top:0"><label style="margin-top:0">Contact E-mail</label><div>you@example.com</div></div>
  <div class="field"><label>Phone Number</label><div>(555) 987 6543</div></div>
  <div class="field"><label>Subjects</label><div>lorem ipsum dolor</div></div>
  <div class="field" style="border:none;height:100px"><label>Your message</label><div>Write your message</div></div>
  <div class="submit">Send Message</div>
</form>

<!-- footer -->
<div class="abs foot foot-links"><a>Contact</a><a>About us</a><a>Products</a></div>
<div class="abs foot" style="left:857px;top:3553px;display:flex;gap:18px;font-size:10px;color:#555"><span>Follow Us:</span><b style="color:#222">f</b><b style="color:#222">t</b><b style="color:#222">ig</b><b style="color:#222">in</b></div>
<div class="abs foot-rule"></div>
<div class="abs foot" style="left:183px;top:3618px;line-height:20px">Northfield Separators, Inc.<br>1450 Harlow Avenue Fairview, WI 53090</div>
<div class="abs foot" style="left:183px;top:3667px;font-size:10px">©2021 Northfield Separators, Inc. All Rights Reserved</div>
<div class="abs legal"><a>Terms of Service</a><a>Privacy Policy</a><a>Site map</a></div>

</body>
</html>
```